GRAPHIC DESIGN FOR RESTAURANT MENU FOR HEALTHY RESTAURANT

I am looking for a graphic design for our menu displayed on a TV screen. Please ensure the file will fit on a TV screen nicely. We are looking for a clean design , with the following items. We would also like to include a couple of photos.
Breakfast:
Protein Chocolate Chip Pancakes - $12.95
Sunny Trail Burrito- $11.95
Tall Barn Omelette - $12.95
Lunch
Butter Chicken - $13.95
Chicken Quesadilla - $13.45
Coconut Garlic Shrimp - $15.95
Goat Cheese Stuffed Chicken - $14.95
Chipotle Steak Wrap - $12.95
Turkey Meatball Fettuccini - $13.45
Chicken Alfredo - $13.45
Chicken Parmesan - $13.95
Pesto Chicken Pasta - $13.45
Steak Bite and Green Stir Fry - $13.45
Asian Chicken Teriyaki - $13.45
Please include our logo
Restaurant

```html
<!DOCTYPE html>
<html lang="en">
<head>
<meta charset="utf-8">
<title>Brightwell Menu Board</title>
<link rel="stylesheet" href="https://fonts.googleapis.com/css2?family=Alfa+Slab+One&family=Roboto+Slab:wght@500;700&family=Roboto+Condensed:wght@500;700&family=Roboto:wght@500;700&display=swap">
<style>
  :root {
    --page: #cfcfcf;
    --board: #141414;
    --board-light: #2e2e2e;
    --lime: #8cc63f;
    --white: #f4f4f4;
    --dots: #cfcfcf;
  }
  * { margin: 0; padding: 0; box-sizing: border-box; }
  html, body { width: 1200px; height: 791px; overflow: hidden; }
  body { background: var(--page); position: relative; }

  .board {
    position: absolute; left: 0; top: 58px;
    width: 1200px; height: 675px; overflow: hidden;
    background:
      radial-gradient(ellipse 45% 55% at 80% 40%, #4a4a4a 0%, rgba(60,60,60,0.4) 40%, transparent 75%),
      radial-gradient(ellipse 60% 70% at 35% 40%, var(--board-light) 0%, var(--board) 80%);
  }

  .section-title {
    position: absolute; left: 37px;
    font-family: "Alfa Slab One", serif;
    color: var(--lime); letter-spacing: 1px; line-height: 1;
  }
  .section-title.lunch { top: 36px; font-size: 62px; }
  .section-title.breakfast { top: 442px; font-size: 60px; }

  .lunch-list {
    position: absolute; left: 37px; top: 124px; width: 720px;
    list-style: none;
  }
  .lunch-item { position: relative; display: flex; align-items: baseline; height: 26.3px; }
  .track { display: flex; align-items: baseline; width: 613px; }
  .item-name {
    font-family: "Roboto Slab", serif; font-weight: 700;
    font-size: 18px; color: var(--white); white-space: nowrap;
  }
  .leader {
    flex: 1 1 auto; min-width: 10px;
    border-bottom: 2px dotted var(--dots); margin-left: 6px;
    transform: translateY(-4px);
  }
  .item-price {
    position: absolute; left: 635px;
    font-family: "Roboto Condensed", sans-serif; font-weight: 700;
    font-size: 20px; color: var(--lime);
  }

  .breakfast-row { position: absolute; left: 37px; top: 517px; }
  .breakfast-item { position: absolute; top: 0; width: 230px; height: 74px; }
  .tag { position: absolute; left: 70px; top: 10px; width: 152px; height: 49px; }
  .tag svg { position: absolute; inset: 0; }
  .tag-name {
    position: absolute; left: 8px; top: 7px;
    font-family: "Roboto Slab", serif; font-weight: 500;
    font-size: 13px; line-height: 17px; color: var(--white); white-space: nowrap;
  }
  .price-badge {
    position: absolute; left: 0; top: 0;
    width: 74px; height: 74px; border-radius: 50%;
    background: var(--lime); border: 4px solid var(--white);
    display: flex; align-items: center; justify-content: center;
    font-family: "Roboto Condensed", sans-serif; font-weight: 700;
    font-size: 18px; color: #1c1c1c;
  }

  .website {
    position: absolute; left: 39px; top: 636px;
    font-family: "Roboto", sans-serif; font-weight: 500;
    font-size: 15px; letter-spacing: 4px; color: var(--white);
  }

  .brand { position: absolute; right: 43px; top: 40px; text-align: right; }
  .brand-name {
    font-family: "Roboto Slab", serif; font-weight: 700;
    font-size: 38px; line-height: 1; color: var(--lime);
  }
  .brand-tagline {
    margin-top: 8px;
    font-family: "Roboto Slab", serif; font-weight: 500;
    font-size: 14px; color: var(--white);
  }

  .food-photo {
    position: absolute; left: 757px; top: 150px; width: 410px; height: 455px;
    border-radius: 40px;
    background: radial-gradient(ellipse 60% 55% at 50% 50%, #c9a27a 0%, #a86a3e 45%, #6b4a36 75%, #2a2a2a 100%);
  }

  .social { position: absolute; top: 624px; right: 40px; display: flex; gap: 14px; }
  .social span { width: 28px; height: 28px; border-radius: 50%; background: var(--lime); }
</style>
</head>
<body>
  <main class="board">
    <h2 class="section-title lunch">LUNCH</h2>
    <ul class="lunch-list">
      <li class="lunch-item"><div class="track"><span class="item-name">Butter Chicken</span><span class="leader"></span></div><span class="item-price">$13.95</span></li>
      <li class="lunch-item"><div class="track"><span class="item-name">Chicken Quesadilla</span><span class="leader"></span></div><span class="item-price">$13.45</span></li>
      <li class="lunch-item"><div class="track"><span class="item-name">Coconut Garlic Shrimp</span><span class="leader"></span></div><span class="item-price">$15.95</span></li>
      <li class="lunch-item"><div class="track"><span class="item-name">Goat Cheese Stuffed Chicken</span><span class="leader"></span></div><span class="item-price">$14.95</span></li>
      <li class="lunch-item"><div class="track"><span class="item-name">Chipotle Steak Wrap</span><span class="leader"></span></div><span class="item-price">$12.95</span></li>
      <li class="lunch-item"><div class="track"><span class="item-name">Turkey Meatball Fettuccini</span><span class="leader"></span></div><span class="item-price">$13.45</span></li>
      <li class="lunch-item"><div class="track"><span class="item-name">Chicken Alfredo</span><span class="leader"></span></div><span class="item-price">$13.45</span></li>
      <li class="lunch-item"><div class="track"><span class="item-name">Chicken Parmesan</span><span class="leader"></span></div><span class="item-price">$13.95</span></li>
      <li class="lunch-item"><div class="track"><span class="item-name">Pesto Chicken Pasta</span><span class="leader"></span></div><span class="item-price">$13.45</span></li>
      <li class="lunch-item"><div class="track"><span class="item-name">Steak Bite and Green Stir Fry</span><span class="leader"></span></div><span class="item-price">$13.45</span></li>
      <li class="lunch-item"><div class="track"><span class="item-name">Asian Chicken Teriyaki</span><span class="leader"></span></div><span class="item-price">$13.45</span></li>
    </ul>

    <h2 class="section-title breakfast">BREAKFAST</h2>
    <div class="breakfast-row">
      <div class="breakfast-item" style="left:0">
        <div class="tag">
          <svg width="152" height="49" viewBox="0 0 152 49"><polyline points="0,1.5 150,1.5 136,47.5 0,47.5" fill="none" stroke="#e8e8e8" stroke-width="1.5" stroke-dasharray="2 2.5"/></svg>
          <div class="tag-name">Protein Chocolate<br>Chip Pancakes</div>
        </div>
        <div class="price-badge">$12.95</div>
      </div>
      <div class="breakfast-item" style="left:235px">
        <div class="tag">
          <svg width="152" height="49" viewBox="0 0 152 49"><polyline points="0,1.5 150,1.5 136,47.5 0,47.5" fill="none" stroke="#e8e8e8" stroke-width="1.5" stroke-dasharray="2 2.5"/></svg>
          <div class="tag-name">Sunny Trail<br>Burrito</div>
        </div>
        <div class="price-badge">$11.95</div>
      </div>
      <div class="breakfast-item" style="left:470px">
        <div class="tag">
          <svg width="152" height="49" viewBox="0 0 152 49"><polyline points="0,1.5 150,1.5 136,47.5 0,47.5" fill="none" stroke="#e8e8e8" stroke-width="1.5" stroke-dasharray="2 2.5"/></svg>
          <div class="tag-name">Tall Barn<br>Omelette</div>
        </div>
        <div class="price-badge">$12.95</div>
      </div>
    </div>

    <p class="website">WWW.BRIGHTWELLKITCHEN.COM</p>

    <div class="brand">
      <div class="brand-name">BRIGHTWELL</div>
      <div class="brand-tagline">Healthy kitchen and meal prep</div>
    </div>

    <div class="food-photo" role="img" aria-label="Photo of chocolate chip pancakes, a steak wrap, an omelette with toast and a bowl of turkey meatball fettuccini"></div>

    <div class="social" aria-label="Social media links">
      <span></span><span></span><span></span>
    </div>
  </main>
</body>
</html>
```